Flyer Design for sewing business

Hi. i need flyers for my new business called " Vora Stitchworks". I am based in Sauchie. I offer Door to Door Clothing Alteration Service!
I provide a door to door alteration service for Clackmannanshire area with 20 miles radiance! (I give free consultations at your preferred location where I can accurately quote the cost of the alteration, as this depends on the garment itself. I aim to deliver the completed item back to you within a week though often it is less than this.)
I also design and sew occasional girls dresses ( first communion, flower girl, party dresses)
The consultation are free with no commitment to take the service.

I wold like see designs that use colors similar to colors on my website, like dusty pink, orange.

To contact either phone MIRA 07912348806
or email: mira.tusk71@quellmail.com

www.brimlink.com/vorastitchworks
www.vora-stitchworks.pagenest.com

THAT IS THE Price List Jeans/Trousers: Shorten....................................from £10.00 Taken in (waist).......................from £8.00 Taken in (side seams)..............from £10.00 Replace zip...............................from £10.00 Dresses/Skirts: Shorten....................................from £10.00 Taken in (waist).......................from £8.00 Taken in (side seams)..............from £8.00 Replace zip...............................from £10.00 Jacket/Coat: Shorten sleeves........................from £12.00 Shorten length (Jacket)...........from £16.00 Shorten length (Coat)..............from £18.00 Taken in (back seam)...............from £12.00 Taken in (side seams)..............from £18.00 Repairs......................................from £5.00 Bridal: Shorten Wedding Dress...........from £25.00 All other bridal alteration quotes can be given on consultation.

Reason: HI, ALL! IN THE NEXT FEW DAYS I GONE EXPERIENCE HOUSE MOVE AND SOME STRESS INVOLVING IN THIS.THANK YOU ALL FOR UNDERSTANDING AND A PATIENCE!

```html
<!DOCTYPE html>
<html lang="en">
<head>
<meta charset="utf-8">
<title>Vora Stitchworks – Door to Door Clothing Alteration Service</title>
<link rel="stylesheet" href="https://fonts.googleapis.com/css2?family=Bree+Serif&family=Gabriela&family=Open+Sans:wght@400&display=swap">
<style>
  :root {
    --paper: #fde8dc;
    --rose: #c9678a;
    --rose-soft: #e3a3b8;
    --rose-deep: #a84a6c;
    --ink: #4b4b4b;
    --link: #4a3f8f;
    --white: #ffffff;
    --stone-1: #8d9296;
    --stone-2: #4f5458;
    --cream-1: #f3ece0;
    --cream-2: #d9cbb4;
  }
  * { margin: 0; padding: 0; box-sizing: border-box; }
  html, body { width: 849px; height: 1200px; overflow: hidden; background: var(--paper); }
  .flyer { position: relative; width: 849px; height: 1200px; background: var(--paper); overflow: hidden; }

  .frame { position: absolute; left: 12px; top: 12px; width: 825px; height: 1176px; border: 3px dashed var(--rose); }

  .flower, .button { position: absolute; border-radius: 50%; }
  .flower { background: var(--rose-soft); }
  .flower--corner { left: 0; top: -13px; width: 150px; height: 150px; }
  .flower--centre { left: 237px; top: 431px; width: 250px; height: 250px; }
  .flower--side { left: 643px; top: 724px; width: 174px; height: 174px; }
  .button { background: var(--rose-soft); }
  .button--a { left: 69px; top: 472px; width: 56px; height: 56px; }
  .button--b { left: 144px; top: 503px; width: 36px; height: 36px; }
  .button--c { left: 770px; top: 338px; width: 40px; height: 40px; }
  .button--d { left: 739px; top: 1075px; width: 56px; height: 56px; }

  .brand { position: absolute; left: 85px; top: 112px; width: 250px; height: 250px; border-radius: 50%; background: var(--white);
    display: flex; align-items: center; justify-content: center; text-align: center; }
  .brand__name { font-family: "Bree Serif", serif; font-size: 24px; letter-spacing: 1px; color: var(--ink); text-transform: uppercase; line-height: 1.2; }

  .hero-photo { position: absolute; left: 275px; top: 15px; width: 555px; height: 403px; transform: rotate(2deg);
    background: linear-gradient(135deg, var(--stone-1), var(--stone-2)); }

  .tape { position: absolute; left: 62px; top: 398px; width: 740px; height: 54px; background: var(--white);
    transform: rotate(3deg); display: flex; align-items: center; justify-content: center; }
  .tape__text { font-family: "Bree Serif", serif; font-size: 29px; color: var(--rose); letter-spacing: 0.5px; }

  .mannequin-photo { position: absolute; left: 75px; top: 549px; width: 225px; height: 593px;
    background: linear-gradient(180deg, var(--cream-1), var(--cream-2)); border-radius: 40% 40% 8px 8px / 12% 12% 8px 8px; }

  .services { position: absolute; font-family: "Gabriela", serif; font-size: 37px; line-height: 54px; color: var(--ink); list-style: none; }
  .services--main { right: 56px; top: 492px; text-align: right; }
  .services--occasion { left: 360px; top: 683px; }

  .promise { position: absolute; left: 333px; top: 918px; width: 391px; height: 75px; background: var(--rose);
    border-radius: 10px; display: flex; align-items: center; justify-content: center; }
  .promise::before { content: ""; position: absolute; inset: 6px; border: 2px dashed var(--white); border-radius: 7px; }
  .promise__text { font-family: "Bree Serif", serif; font-size: 28px; color: var(--white); text-shadow: 2px 2px 0 var(--rose-deep); }

  .contact { position: absolute; left: 258px; top: 1002px; width: 540px; text-align: center; font-family: "Open Sans", sans-serif; color: var(--ink); }
  .contact__web { font-size: 29px; color: var(--link); text-decoration: underline; line-height: 44px; }
  .contact__social { font-size: 19px; color: var(--link); text-decoration: underline; line-height: 32px; }
  .contact__line { font-size: 19px; line-height: 32px; }
  .contact__email { color: var(--link); text-decoration: underline; }
</style>
</head>
<body>
<main class="flyer">
  <div class="flower flower--corner" role="img" aria-label="Dusty pink decorative flower"></div>
  <div class="frame"></div>

  <div class="hero-photo" role="img" aria-label="Photo of a dress form sketch stitched on a notebook with thread spools on a grey stone surface"></div>

  <div class="brand">
    <span class="brand__name">Vora<br>Stitchworks</span>
  </div>

  <div class="button button--c" role="img" aria-label="Pink sewing button"></div>

  <div class="tape"><span class="tape__text">Door to Door Clothing Alteration Service</span></div>

  <div class="button button--a" role="img" aria-label="Pink sewing button"></div>
  <div class="button button--b" role="img" aria-label="Pink sewing button"></div>
  <div class="flower flower--centre" role="img" aria-label="Dusty pink decorative flower"></div>
  <div class="flower flower--side" role="img" aria-label="Dusty pink decorative flower"></div>

  <div class="mannequin-photo" role="img" aria-label="Photo of a tailor's mannequin draped with tape measures and scissors"></div>

  <ul class="services services--main">
    <li>Fashion Designer</li>
    <li>Fashion Consultant</li>
    <li>Alterations</li>
    <li>Weddings</li>
  </ul>

  <ul class="services services--occasion">
    <li>Christenings</li>
    <li>First Communion</li>
    <li>Flower Girl</li>
    <li>Party Dresses</li>
  </ul>

  <div class="promise"><span class="promise__text">Fast and Reliable Service</span></div>

  <div class="contact">
    <p class="contact__web">www.vora-stitchworks.pagenest.com</p>
    <p class="contact__social">www.brimlink.com/vorastitchworks</p>
    <p class="contact__line">Phone: Mira 07912348806</p>
    <p class="contact__line">Email: <span class="contact__email">mira.tusk71@quellmail.com</span></p>
  </div>

  <div class="button button--d" role="img" aria-label="Pink sewing button"></div>
</main>
</body>
</html>
```